Alpenmark Banner

Hi boys and girls :)

We have a little project 4u.

We need a banner in 4 sizes :

Leaderboard: 728*90
Wide SkyScraper: 160*600
Medium Rectangle: 300*250
Ribbon (special format): 990*45

Message on banner :

Either our Logo + Immigration, Integration, Naturalization

Or our Logo + Incorporation, Domicile, Secretarial Services

And if space allows for it www.alpenmark-example.com as well.

We are looking for a clean design, check our Website for inspiration concerning colors.

```html
<!DOCTYPE html>
<html lang="en">
<head>
<meta charset="utf-8">
<title>Alpenmark Leaderboard Banner</title>
<link rel="stylesheet" href="https://fonts.googleapis.com/css2?family=Tinos:ital,wght@0,400;1,400&family=Arimo:wght@700&display=swap">
<style>
  :root {
    --brand-red: #d7141a;
    --button-red: #e3201c;
    --button-red-dark: #b00c0c;
    --panel-dark: #262626;
    --panel-mid: #3a3a3a;
    --photo-white: #e6e6e6;
    --photo-light: #c4c4c4;
    --photo-mid: #9a9a9a;
    --photo-shade: #6e6e6e;
    --photo-dark: #3d3d3d;
    --white: #ffffff;
    --divider: #d4d4d4;
  }
  * { margin: 0; padding: 0; box-sizing: border-box; }
  html, body { width: 1200px; height: 148px; overflow: hidden; background: var(--white); }
  .banner {
    position: relative;
    width: 1200px;
    height: 148px;
    overflow: hidden;
    background: var(--divider);
  }
  .street-photo {
    position: absolute;
    left: 0; top: 0;
    width: 462px; height: 148px;
    background:
      linear-gradient(180deg, rgba(255,255,255,0.25) 0%, rgba(255,255,255,0) 45%, rgba(0,0,0,0.12) 100%),
      linear-gradient(90deg,
        var(--photo-light) 0%, var(--photo-white) 10%, var(--photo-mid) 24%,
        var(--photo-dark) 34%, var(--photo-shade) 42%, var(--photo-white) 55%,
        var(--photo-light) 68%, var(--photo-shade) 80%, var(--photo-dark) 92%, var(--photo-mid) 100%);
  }
  .arcade-photo {
    position: absolute;
    left: 800px; top: 0;
    width: 400px; height: 148px;
    background:
      linear-gradient(180deg, rgba(0,0,0,0.1) 0%, rgba(255,255,255,0) 50%, rgba(0,0,0,0.15) 100%),
      linear-gradient(90deg,
        var(--photo-shade) 0%, var(--photo-light) 12%, var(--photo-mid) 26%,
        var(--photo-dark) 36%, var(--photo-shade) 50%, var(--photo-light) 70%,
        var(--photo-white) 82%, var(--photo-mid) 100%);
  }
  .brand {
    position: absolute;
    left: 10px; top: 6px;
    display: flex;
    align-items: center;
    gap: 8px;
    padding: 6px 10px 6px 6px;
    background: rgba(255,255,255,0.55);
  }
  .brand-mark {
    width: 26px; height: 26px;
    background: var(--brand-red);
  }
  .brand-name {
    font-family: "Tinos", serif;
    font-weight: 400;
    font-size: 30px;
    line-height: 1;
    color: var(--brand-red);
  }
  .message-panel {
    position: absolute;
    left: 465px; top: 0;
    width: 332px; height: 148px;
    background: linear-gradient(180deg, var(--panel-mid) 0%, var(--panel-dark) 100%);
    padding: 20px 0 0 30px;
    font-family: "Tinos", serif;
    font-style: italic;
    line-height: 1;
    white-space: nowrap;
  }
  .message-panel p { color: var(--white); }
  .service-primary { font-size: 32px; }
  .service-accent { font-size: 46px; color: var(--brand-red) !important; margin-top: 0; }
  .service-secondary { font-size: 38px; margin-top: -2px; }
  .cta-button {
    position: absolute;
    left: 873px; top: 46px;
    width: 276px; height: 60px;
    border-radius: 8px;
    background: linear-gradient(180deg, var(--button-red) 0%, var(--button-red-dark) 100%);
    display: flex;
    align-items: center;
    justify-content: space-between;
    padding: 0 14px 0 22px;
    font-family: "Arimo", sans-serif;
    font-weight: 700;
    font-size: 20px;
    color: var(--white);
    text-decoration: none;
    box-shadow: 0 3px 6px rgba(0,0,0,0.4);
  }
  .cta-icon { width: 34px; height: 34px; }
</style>
</head>
<body>
  <div class="banner">
    <div class="street-photo" role="img" aria-label="Black and white photo of an old town street with parked bicycles, trees and arcades"></div>
    <div class="brand">
      <span class="brand-mark"></span>
      <span class="brand-name">Alpenmark</span>
    </div>

    <div class="message-panel">
      <p class="service-primary">Immigration,</p>
      <p class="service-accent">Integration,</p>
      <p class="service-secondary">Naturalization</p>
    </div>

    <div class="arcade-photo" role="img" aria-label="Black and white photo of a stone arcade and facade in an old town"></div>

    <a class="cta-button" href="#">
      <span>FIND OUT MORE</span>
      <svg class="cta-icon" viewBox="0 0 34 34" aria-hidden="true">
        <circle cx="17" cy="17" r="15" fill="#7a0a0a" stroke="#ffffff" stroke-width="2"/>
        <path d="M14 10 L21 17 L14 24" fill="none" stroke="#ffffff" stroke-width="3.5" stroke-linecap="round" stroke-linejoin="round"/>
      </svg>
    </a>
  </div>
</body>
</html>
```